Amazing Website for innovative Tax-App

Background:
Our Company "Rendolo" provides all employees an App, that allows them to file their tax easy, in only a few minutes and most importantly without any prior knowledge. Most people miss out on their well deserved tax refund. Rendolo helps these people to not only get back their money, but also to maximise their refund.
Task:
Please help us create a beautiful and high quality Webdesign with breathtaking mockups, which immediately reflects what rendolo stands for.
Rendolo is THE tool for getting back tax money (could have a slightly official government touch)
Rendolo breaks down complex old procedures in the utmost easiest way, so that filing your tax via app with a few clicks becomes almost fun.
Additional:
Please surprise us with great mockups, that showcases our app, maybe some icons that reflects users individual life and flying around. (Taxes are as individual as users life!
Maybe catch people with a notification that shows that in your online banking you got around 1000€ in refund and create excitement that "you could be the next"
Work with the newest iphone devices as mockup and use screenshots that are provided in files. You can also think of creating some 3D elements around the phone.
this is how our current website looks like: www.rendolo-beispiel.at
You can take inspirations from that existing site.
Plus, this is is a website from another company in the same field that we like: https://www.kassmiro-beispiel.com/
Please provide complete desktop and mobile website Design and most importantly..
Please be creative!

```html
<!DOCTYPE html>
<html lang="en">
<head>
<meta charset="utf-8">
<title>Rendolo – Get Your Tax Return Easily</title>
<link href="https://fonts.googleapis.com/css2?family=Manrope:wght@400;500;600;700;800&display=swap" rel="stylesheet">
<style>
:root{
  --stage:#121614;
  --ink:#0f1a24;
  --muted:#7a8791;
  --teal:#14bfa6;
  --teal-dark:#0aa894;
  --green:#3ed07a;
  --mint:#e3f8f1;
  --lime:#e9f7c8;
  --cyan:#35c9e0;
  --cyan-2:#2ee6dc;
  --white:#ffffff;
  --card:#fbfefd;
  --star:#f5b400;
  --coral:#f2735a;
}
*{box-sizing:border-box;margin:0;padding:0}
html,body{width:1200px;height:1200px;overflow:hidden;background:var(--stage);font-family:"Manrope",sans-serif;color:var(--ink)}
.page{position:absolute;left:429px;top:59px;width:550px;height:1742px;transform:scale(.621);transform-origin:0 0;background:var(--white);overflow:hidden}
.abs{position:absolute}
/* hero */
.hero{left:0;top:0;width:550px;height:308px;background:radial-gradient(circle at 30% 30%,#f3fbef 0,transparent 55%),radial-gradient(circle at 75% 35%,var(--lime) 0,transparent 45%),linear-gradient(160deg,#dff7ef 0%,#eef9e6 50%,#cdf2ea 100%)}
.nav-logo{left:79px;top:10px;font-weight:800;font-size:13px;color:var(--teal);display:flex;align-items:center;gap:4px}
.dot{display:inline-block;width:12px;height:12px;border-radius:50%;background:var(--teal)}
.nav-link{top:15px;font-size:5.5px;font-weight:500}
.lang{left:404px;top:11px;width:22px;height:13px;border-radius:7px;background:var(--white);font-size:5px;text-align:center;line-height:13px}
.login{left:431px;top:11px;width:39px;height:13px;border-radius:7px;background:var(--cyan);color:var(--white);font-size:5px;text-align:center;line-height:13px}
.hero-title{left:79px;top:78px;font-size:33px;font-weight:700;line-height:37px;letter-spacing:-.5px}
.hero-title .accent{background:linear-gradient(90deg,var(--teal),var(--green));-webkit-background-clip:text;background-clip:text;color:transparent}
.hero-sub{left:79px;top:163px;font-size:9.5px;font-weight:500}
.store{height:23px;width:71px;border-radius:12px;background:var(--white);box-shadow:0 3px 8px rgba(0,0,0,.06);display:flex;align-items:center;justify-content:center;gap:5px;font-size:6px;font-weight:600}
.store i{width:8px;height:8px;border-radius:50%;background:var(--ink);display:block}
.rating{left:79px;top:238px;display:flex;gap:6px;align-items:flex-start}
.rating .badge{width:17px;height:17px;border-radius:50%;background:var(--white)}
.rating .stars{color:var(--star);font-size:7px;letter-spacing:1px}
.rating .stars b{color:var(--ink);font-size:5px;font-weight:600;letter-spacing:0}
.rating small{display:block;font-size:4px;color:var(--muted)}
.hero-photo{left:318px;top:34px;width:160px;height:274px;border-radius:80px 80px 0 0;background:linear-gradient(180deg,#3a2a20 0%,#8a5a33 35%,#9b5e2c 60%,#3e5a8a 100%);opacity:.85}
.refund-card{left:313px;top:150px;width:56px;height:29px;border-radius:4px;background:rgba(255,255,255,.55);padding:5px 7px}
.refund-card small{display:block;font-size:4px}
.refund-card b{font-size:8px;font-weight:700}
.ball{border-radius:50%;background:radial-gradient(circle at 35% 30%,#b9f7c8,var(--green))}
.ball.blue{background:radial-gradient(circle at 35% 30%,#d8ecff,#7fb6e8)}
/* benefits */
.benefits{left:0;top:308px;width:550px;height:277px;background:linear-gradient(160deg,#f7fdf9 0%,#eef8e7 45%,#e6f7ef 100%)}
.h2{left:0;width:550px;text-align:center;font-size:16.5px;font-weight:700;letter-spacing:-.2px}
.card{top:381px;width:124px;height:167px;border-radius:6px;background:var(--card);box-shadow:0 4px 14px rgba(20,120,100,.07);padding:12px}
.card .ico{width:30px;height:30px;border-radius:50%;border:1px solid #cdeee6;display:flex;align-items:center;justify-content:center;margin-bottom:10px}
.card .ico span{width:10px;height:10px;border-radius:3px;background:var(--teal)}
.card h3{font-size:9px;font-weight:700;margin-bottom:8px}
.card p{font-size:4.6px;line-height:8.2px;color:var(--muted)}
/* testimonials */
.eyebrow{left:0;width:550px;text-align:center;top:623px;font-size:4px;font-weight:700;color:var(--teal);letter-spacing:.3px}
.t-photo{left:92px;top:686px;width:138px;height:164px;background:linear-gradient(180deg,#eaf1fb 0%,#d8c8b6 40%,#7a7352 100%)}
.t-corner{left:206px;top:827px;width:46px;height:46px;border-radius:0 0 46px 0;background:linear-gradient(135deg,var(--cyan-2),var(--teal))}
.t-arrow{width:16px;height:16px;border-radius:50%;background:var(--white);box-shadow:0 2px 6px rgba(0,0,0,.12);font-size:8px;text-align:center;line-height:16px}
.quote-mark{left:282px;top:694px;font-size:16px;color:var(--coral);font-weight:800}
.q-stars{left:282px;top:712px;color:var(--coral);font-size:8px;letter-spacing:1px}
.quote{left:282px;top:729px;width:192px;font-size:9.2px;line-height:14px;font-weight:500}
.author{left:283px;top:801px;font-size:6px;font-weight:700}
.author small{display:block;font-weight:400;color:var(--teal);font-size:4.6px;margin-top:3px}
.partner{left:419px;top:807px;font-size:8px;color:#b8c2c8;font-weight:600}
/* more */
.more{left:0;top:885px;width:550px;height:460px;background:linear-gradient(180deg,#ffffff 0%,#ddf6ea 25%,#e5f6df 55%,#ffffff 90%)}
.desc{left:140px;width:270px;text-align:center;font-size:5px;line-height:8px;color:var(--muted)}
.phone{top:1021px;border-radius:10px;background:var(--teal);overflow:hidden;color:var(--white)}
.phone.center{left:213px;top:1016px;width:122px;height:250px;border:4px solid #1b2228;border-radius:16px;background:var(--white)}
.screen-top{height:178px;background:var(--teal);padding:12px 8px;text-align:center}
.screen-top h4{font-size:7px;font-weight:700;margin-top:68px}
.screen-top p{font-size:4px;margin-top:4px;opacity:.9}
.screen-top .amt{font-size:13px;font-weight:800;margin-top:14px}
.btn-weiter{margin:20px 10px 0;height:12px;border-radius:6px;background:var(--teal);color:var(--white);font-size:4.5px;text-align:center;line-height:12px}
.ui-row{height:8px;border-radius:4px;background:#e7f6f3;margin:4px 6px}
.ui-pill{height:7px;width:36px;border-radius:4px;background:#8fded3;margin:5px 0 0 auto}
/* customers */
.customers{left:0;width:550px;text-align:center;top:1311px;font-size:6.5px;font-weight:500}
.press{top:1334px;width:24px;height:12px;border-radius:2px;background:#c9cfd3}
/* cta */
.cta{left:27px;top:1373px;width:495px;height:240px}
.cta-title{left:0;width:550px;text-align:center;top:1434px;font-size:16px;font-weight:700;color:var(--white)}
/* footer */
.footer{left:0;top:1560px;width:550px;height:182px;background:linear-gradient(180deg,transparent 0,#e6f7f1 40%,#dff4ec 100%)}
.f-col{top:1640px}
.f-col h5{font-size:7.5px;font-weight:700;margin-bottom:10px}
.f-col a,.f-col p{display:block;font-size:4.8px;color:var(--muted);text-decoration:none;line-height:12px}
.f-col p{line-height:8px}
.social{display:flex;gap:6px;margin-top:8px}
.social span{width:7px;height:7px;border-radius:1px;background:var(--teal)}
</style>
</head>
<body>
<main class="page">

  <!-- HERO -->
  <section class="abs hero"></section>
  <div class="abs ball" style="left:52px;top:64px;width:8px;height:8px"></div>
  <div class="abs ball" style="left:322px;top:62px;width:14px;height:14px"></div>
  <div class="abs ball" style="left:20px;top:231px;width:10px;height:10px"></div>
  <div class="abs ball blue" style="left:472px;top:89px;width:20px;height:20px"></div>
  <div class="abs hero-photo" role="img" aria-label="Photo of a delighted young woman looking at her smartphone"></div>
  <div class="abs refund-card"><small>Tax refunded</small><b>€1000</b></div>

  <div class="abs nav-logo"><span class="dot"></span>rendolo</div>
  <a class="abs nav-link" style="left:253px">Our Vision</a>
  <a class="abs nav-link" style="left:305px">Benefits</a>
  <a class="abs nav-link" style="left:352px">It's that easy!</a>
  <div class="abs lang">En ▾</div>
  <div class="abs login">Login</div>

  <h1 class="abs hero-title">Get Your Tax<br><span class="accent">Return Easily</span></h1>
  <p class="abs hero-sub">€748 refund in less than 8 minutes</p>
  <div class="abs store" style="left:79px;top:192px"><i></i>Appvento</div>
  <div class="abs store" style="left:156px;top:192px"><i></i>Spielmarkt</div>
  <div class="abs rating">
    <span class="badge"></span>
    <div><div class="stars">★★★★★ <b>4.9/5 Star</b></div><small>Based on 1254 reviews</small></div>
  </div>

  <!-- BENEFITS -->
  <section class="abs benefits"></section>
  <div class="abs ball" style="left:0;top:512px;width:16px;height:16px"></div>
  <h2 class="abs h2" style="top:344px">Clear Benefits</h2>
  <article class="abs card" style="left:78px">
    <div class="ico"><span></span></div>
    <h3>Simple</h3>
    <p>Rendolo Is Easy To Use And Convenient. Even Beginners To The Tax World Can Feel Like A Pro! Rendolo Will Guide You Through All Relevant Questions, Calculate Your Maximum Refund And Transfer Your Money Directly To Your Account. Rendolo Gives You Peace Of Mind Knowing That Your Taxes Are Done Right The First Time! It Can Be Accessed Anytime, Anywhere.</p>
  </article>
  <article class="abs card" style="left:213px">
    <div class="ico"><span></span></div>
    <h3>Legally Secure</h3>
    <p>Rendolo Is 100% Legally Secure And Protected. Your Data Is Treated As Strictly Confidential. All Confidential Data Is Transmitted Through The Austrian Tax Office Via Our Secure And Protected Interface. Your Security Is Built Into Everything We Do.</p>
  </article>
  <article class="abs card" style="left:347px">
    <div class="ico"><span></span></div>
    <h3>Cost Efficient</h3>
    <p>The Best Part About Our Services Is That It Is At No Cost To You. Rendolo Is A 100% Free Service. There Are Zero Fees And Costs To Filing Your Tax Returns Using Rendolo. Only At The Time You Receive Your Tax Returns, Rendolo Will Redeem 10% To Cover Processing Service Fees. This Service Pays For Itself.</p>
  </article>

  <!-- TESTIMONIALS -->
  <p class="abs eyebrow">TESTIMONIALS</p>
  <h2 class="abs h2" style="top:633px">Check What Our Clients Are Saying</h2>
  <div class="abs t-corner"></div>
  <div class="abs t-photo" role="img" aria-label="Photo of a smiling woman with glasses using her phone"></div>
  <div class="abs t-arrow" style="left:84px;top:757px">‹</div>
  <div class="abs t-arrow" style="left:221px;top:756px">›</div>
  <div class="abs quote-mark">“</div>
  <div class="abs q-stars">★★★★★</div>
  <p class="abs quote">Is be upon sang fond must shew. Really boy law county she unable her sister. Feet you off its like like six. Among sex are leave law built now.</p>
  <div class="abs author">Mara Selin<small>CEO Brightfold</small></div>
  <div class="abs partner">Lumora</div>

  <!-- MORE -->
  <section class="abs more"></section>
  <div class="abs ball blue" style="left:476px;top:895px;width:20px;height:20px"></div>
  <div class="abs ball" style="left:78px;top:977px;width:9px;height:9px"></div>
  <h2 class="abs h2" style="top:951px">With Us You Will Get More</h2>
  <p class="abs desc" style="top:979px">Compared To Steuerportal, Rendolo Shows You In A Playful Way What You Can Claim For Tax Refund Based On Your Everyday Life. Our Intelligent Question-Algorithm Creates Added Value For You And Maximises Your Tax Refund – So Why Settle For Less?</p>

  <div class="abs phone" style="left:-10px;width:74px;height:198px;background:var(--white);border:1px solid #e3ecea">
    <div style="height:30px;background:var(--teal);font-size:7px;font-weight:700;padding:18px 0 0 10px">ex!</div>
    <div class="ui-row" style="background:var(--teal);height:14px"></div>
    <div class="ui-pill"></div><div class="ui-pill"></div><div class="ui-pill"></div>
    <div class="ui-row" style="margin-top:16px"></div>
  </div>
  <div class="abs phone" style="left:96px;width:92px;height:198px;background:var(--white);border:1px solid #e3ecea">
    <div style="height:36px;background:var(--teal);text-align:center;font-size:5px;font-weight:700;padding-top:16px">0,00 €</div>
    <div class="ui-row" style="background:var(--teal);height:12px"></div>
    <div style="margin:4px 6px;height:88px;border-radius:4px;border:1px solid #e3ecea;padding:6px;color:var(--ink);font-size:4.5px;line-height:7px">Hast du schon mal eine Steuererklärung abgegeben?<div class="ui-row" style="margin:8px 0 0;background:#8fded3"></div><div class="ui-row" style="margin:3px 0"></div></div>
    <div class="ui-row"></div><div class="ui-row"></div>
  </div>
  <div class="abs phone center">
    <div class="screen-top">
      <h4>Gratuliere, Lena!</h4>
      <p>Deine voraussichtliche Rückzahlung im Jahr 2022 beträgt</p>
      <div class="amt">861,70 €</div>
    </div>
    <p style="font-size:4px;color:var(--teal);text-align:center;margin-top:12px">So berechnen wir dein Ergebnis</p>
    <div class="btn-weiter">weiter</div>
  </div>
  <div class="abs phone" style="left:362px;width:92px;height:198px">
    <svg class="abs" style="left:34px;top:86px" width="24" height="20" viewBox="0 0 24 20"><path d="M2 10 L22 2 L14 18 L11 11 Z" fill="#fff"/></svg>
    <div class="abs" style="left:20px;top:163px;width:50px;height:2px;background:#fff"></div>
  </div>
  <div class="abs phone" style="left:486px;width:74px;height:198px;background:var(--white);border:1px solid #e3ecea">
    <div style="height:145px;background:var(--teal);text-align:center;padding-top:56px">
      <svg width="32" height="32" viewBox="0 0 32 32"><circle cx="16" cy="16" r="15" fill="#fff"/><path d="M9 16 L14 21 L23 11" stroke="#14bfa6" stroke-width="3" fill="none"/></svg>
      <p style="font-size:6px;font-weight:700;margin-top:6px">Geschafft!</p>
    </div>
    <div class="ui-row" style="margin-top:26px;background:var(--teal)"></div>
  </div>

  <p class="abs customers">Thousands Of Satisfied Customers</p>
  <div class="abs press" style="left:156px"></div>
  <div class="abs press" style="left:210px"></div>
  <div class="abs press" style="left:263px;width:34px"></div>
  <div class="abs press" style="left:319px;width:18px;height:16px;top:1332px"></div>
  <div class="abs press" style="left:368px"></div>

  <!-- CTA -->
  <section class="abs footer"></section>
  <svg class="abs cta" viewBox="0 0 495 240" aria-hidden="true">
    <defs><linearGradient id="ctaGrad" x1="0" y1="0" x2="0" y2="1"><stop offset="0" stop-color="#35c2df"/><stop offset="1" stop-color="#3eeadf"/></linearGradient></defs>
    <path d="M0 0 L247 27 L495 0 L495 120 Q495 150 460 165 L247 240 L35 165 Q0 150 0 120 Z" fill="url(#ctaGrad)"/>
    <circle cx="425" cy="130" r="50" fill="#ffffff" opacity=".12"/>
    <circle cx="80" cy="145" r="26" fill="#ffffff" opacity=".15"/>
    <circle cx="50" cy="68" r="6" fill="#3ed07a"/>
    <circle cx="456" cy="78" r="4" fill="#3ed07a"/>
  </svg>
  <h2 class="abs cta-title">Your Tax Refund With A Few Clicks</h2>
  <p class="abs desc" style="top:1462px;color:#eafdfb">Compared To Steuerportal, Rendolo Shows You In A Playful Way What You Can Claim For Tax Refund Based On Your Everyday Life. Our Intelligent Question-Algorithm Creates Added Value For You And Maximises Your Tax Refund – So Why Settle For Less?</p>
  <div class="abs store" style="left:201px;top:1505px"><i></i>Appvento</div>
  <div class="abs store" style="left:278px;top:1505px"><i></i>Spielmarkt</div>
  <div class="abs ball blue" style="left:36px;top:1578px;width:22px;height:22px"></div>
  <div class="abs ball blue" style="left:354px;top:1540px;width:14px;height:14px"></div>
  <div class="abs ball" style="left:516px;top:1643px;width:12px;height:12px"></div>

  <!-- FOOTER -->
  <div class="abs f-col" style="left:79px;width:80px">
    <h5>Über Uns</h5>
    <p>More Than 80% Of People In Our Country Do Not Apply For Tax Returns That They Are Entitled To.</p>
    <div class="social"><span></span><span></span><span></span><span></span></div>
  </div>
  <div class="abs f-col" style="left:212px"><h5>Wissenswert</h5><a>FAQ</a><a>Ratgeber</a><a>Für Unternehmen</a><a>Für Steuerberater</a></div>
  <div class="abs f-col" style="left:310px"><h5>Wer Wir Sind</h5><a>Presse</a><a>Vision</a><a>Kontakt</a><a>Karriere</a></div>
  <div class="abs f-col" style="left:406px"><h5>Weiteres</h5><a>Impressum</a><a>AGB</a><a>Nutzungsvereinbarung</a><a>Datenschutz</a></div>
</main>
</body>
</html>
```